Fitness Company Valentine's Day Special Flyer

We need an 8x10 flyer designed for our Valentine's Day Special Promo offer to the public. We've included the flyer's text and details - please include all information in the word document attached. DO NOT use this as a design template just the information. We expect something awesome!!!
- The flyer MUST be 8x10 in PSD format (CS3 Compatible) INCLUDING ALL Layers and Fonts
- Please include fitness pictures
- Include our Logo (attached)
- ***Please use the color schemes used in our logo to help with the design!!!!
Industry/Entity Type
Fitness
Look and feel
Each slider illustrates characteristics of the customer's brand and the style your logo design should communicate.

```html
<!DOCTYPE html>
<html lang="en">
<head>
<meta charset="utf-8">
<title>Valentine's Day 2-for-1 Special Flyer</title>
<link rel="stylesheet" href="https://fonts.googleapis.com/css2?family=Anton&family=Kaushan+Script&family=Oswald:wght@500&family=Signika:wght@600;700&family=Open+Sans:wght@700;800&display=swap">
<style>
  :root {
    --magenta: #c21ec8;
    --magenta-deep: #8c0f93;
    --violet: #a52ab8;
    --pink-soft: #f0a8ee;
    --red: #d8101e;
    --charcoal: #3b3b3d;
    --white: #ffffff;
    --ink: #111111;
    --stage: #e6e6e6;
    --gold: #ffd23a;
  }
  * { box-sizing: border-box; margin: 0; padding: 0; }
  html, body { width: 1200px; height: 1200px; overflow: hidden; }
  body { background: var(--stage); font-family: "Signika", sans-serif; }

  .flyer {
    position: absolute; left: 144px; top: 30px;
    width: 912px; height: 1140px; overflow: hidden;
    background: var(--magenta);
  }
  .flyer-bg {
    position: absolute; inset: 0;
    background: radial-gradient(ellipse at 35% 40%, #e24fe6 0%, #b414bd 45%, #7a0b82 100%);
  }
  .art { position: absolute; inset: 0; width: 912px; height: 1140px; }

  .brand {
    position: absolute; left: 32px; top: 49px; width: 301px; height: 95px;
    background: var(--white); border: 4px solid var(--ink);
    display: flex; align-items: center; justify-content: center;
    font-family: "Oswald", sans-serif; font-weight: 500; font-size: 36px;
    color: var(--ink); letter-spacing: 1px;
  }

  .call-bar {
    position: absolute; left: 379px; top: 77px; width: 533px; height: 79px;
    color: var(--white); font-family: "Open Sans", sans-serif; font-weight: 700;
    font-size: 23px; line-height: 31px; text-align: center; padding-top: 8px; padding-left: 20px;
  }

  .headline { position: absolute; left: 24px; font-family: "Anton", sans-serif; color: var(--red);
    text-shadow: 3px 3px 0 var(--white); line-height: 1; white-space: nowrap; transform-origin: top left; }
  .headline--day { top: 170px; font-size: 92px; letter-spacing: -1px; transform: scale(1.18, 0.9); }
  .headline--offer { top: 262px; font-size: 118px; letter-spacing: -3px; transform: scale(1.15, 0.9); }
  .script-special { position: absolute; font-family: "Kaushan Script", cursive; color: var(--white);
    line-height: 1; text-shadow: 2px 3px 4px rgba(0,0,0,.4); white-space: nowrap; }
  .script-special--hero { left: 22px; top: 372px; font-size: 118px; transform: rotate(-14deg); }
  .script-special--badge { left: 88px; top: 812px; font-size: 50px; transform: rotate(-20deg); }

  .gift-label {
    position: absolute; left: 448px; top: 412px; width: 420px;
    color: var(--white); font-family: "Open Sans", sans-serif; font-weight: 700;
    font-size: 16.5px; line-height: 21px;
  }

  .perks { position: absolute; left: 398px; top: 488px; width: 500px; list-style: none;
    font-family: "Oswald", sans-serif; font-weight: 500; color: var(--white);
    font-size: 29px; line-height: 33px; letter-spacing: 1.4px; text-transform: uppercase; white-space: nowrap; }
  .perks li { position: relative; padding-left: 35px; margin-bottom: 1px; }
  .perks svg { position: absolute; left: 0; top: 10px; width: 20px; height: 18px; }

  .tagline-couples { position: absolute; left: 24px; top: 546px; color: var(--white);
    font-weight: 700; font-size: 41px; line-height: 47px; text-shadow: 2px 2px 3px rgba(0,0,0,.35); }

  .brush-label { position: absolute; left: 3px; top: 727px; width: 262px; height: 68px;
    color: var(--violet); font-family: "Open Sans", sans-serif; font-weight: 800;
    font-size: 22px; line-height: 23px; padding: 8px 0 0 28px; }

  .price-badge { position: absolute; left: 172px; top: 850px; transform: rotate(-18deg);
    font-family: "Open Sans", sans-serif; font-weight: 800; color: var(--gold); text-align: center; }
  .price-badge__only { font-size: 24px; line-height: 1; }
  .price-badge__amount { font-size: 40px; line-height: 1.05; }

  .train-bar { position: absolute; left: 304px; top: 750px; width: 608px; height: 42px;
    background: var(--pink-soft); color: var(--violet); font-weight: 600; font-size: 29px;
    line-height: 42px; padding-left: 48px; }

  .slogan-pill { position: absolute; left: 119px; top: 979px; width: 729px; height: 63px;
    background: var(--pink-soft); border-radius: 10px; color: var(--ink);
    font-family: "Open Sans", sans-serif; font-weight: 800; font-size: 27px;
    line-height: 63px; text-align: center; }

  .expiry { position: absolute; left: 0; top: 1052px; width: 912px; text-align: center;
    color: var(--white); font-family: "Open Sans", sans-serif; font-weight: 700; font-size: 24px; }
  .footer { position: absolute; left: 0; top: 1100px; width: 912px; text-align: center;
    color: var(--white); font-family: "Open Sans", sans-serif; font-weight: 700; font-size: 18.5px; }
</style>
</head>
<body>
<main class="flyer">
  <div class="flyer-bg" role="img" aria-label="Magenta-tinted photo of a muscular athlete training with weights"></div>

  <svg class="art" viewBox="0 0 912 1140">
    <defs>
      <linearGradient id="treadmillPhoto" x1="0" y1="0" x2="1" y2="1">
        <stop offset="0" stop-color="#c9d3dc"/><stop offset=".6" stop-color="#e7c7b8"/><stop offset="1" stop-color="#b23a3a"/>
      </linearGradient>
      <linearGradient id="groupPhoto" x1="0" y1="0" x2="1" y2="0">
        <stop offset="0" stop-color="#e9eef2"/><stop offset=".3" stop-color="#5a86c9"/><stop offset=".55" stop-color="#f2a7c6"/><stop offset=".8" stop-color="#4d5a70"/><stop offset="1" stop-color="#7fd3d6"/>
      </linearGradient>
      <linearGradient id="slate" x1="0" y1="0" x2="1" y2="1">
        <stop offset="0" stop-color="#2f2f31"/><stop offset=".5" stop-color="#4a4a4c"/><stop offset="1" stop-color="#2b2b2d"/>
      </linearGradient>
    </defs>

    <polygon points="780,0 912,0 912,45 835,100" fill="#d9d9d9"/>
    <line x1="745" y1="95" x2="870" y2="0" stroke="#fff" stroke-width="3"/>
    <line x1="770" y1="100" x2="890" y2="10" stroke="#fff" stroke-width="2"/>

    <polygon points="400,77 912,77 912,156 379,156" fill="var(--violet)"/>
    <line x1="379" y1="156" x2="912" y2="156" stroke="#fff" stroke-width="2"/>

    <g role="img" aria-label="Photo of women running on treadmills in a gym">
      <polygon points="760,158 912,158 912,381 540,381" fill="url(#treadmillPhoto)"/>
    </g>
    <line x1="540" y1="381" x2="760" y2="158" stroke="#fff" stroke-width="3"/>

    <polygon points="340,527 485,381 912,381 912,748 340,748" fill="url(#slate)"/>
    <polyline points="330,748 330,523 480,373" fill="none" stroke="#d94fe0" stroke-width="3"/>
    <polygon points="430,407 875,407 855,463 415,463" fill="var(--violet)"/>
    <polygon points="880,407 892,407 872,463 860,463" fill="var(--violet)"/>
    <polygon points="898,407 910,407 890,463 878,463" fill="var(--violet)"/>

    <g role="img" aria-label="Photo of smiling couples in workout clothes holding dumbbells">
      <rect x="308" y="792" width="604" height="188" fill="url(#groupPhoto)"/>
    </g>

    <line x1="0" y1="1082" x2="330" y2="748" stroke="#fff" stroke-width="2"/>

    <path d="M3,735 Q60,722 130,730 T262,728 L258,792 Q170,800 90,790 T3,795 Z" fill="#c9c9c9"/>

    <path transform="translate(25,-5)" d="M200,948 C150,905 105,880 112,842 C118,812 152,802 172,826 C180,796 222,790 236,818 C252,852 228,900 200,948 Z" fill="var(--red)" stroke="#fff" stroke-width="3"/>

    <rect x="0" y="990" width="912" height="150" fill="var(--magenta)"/>
  </svg>

  <div class="brand">Pulsora Bootcamps</div>
  <div class="call-bar">Call Us Now at<br>555-014-2876 to Reserve This Offer!</div>

  <h1>
    <span class="headline headline--day">VALENTINE'S DAY</span>
    <span class="headline headline--offer">2-FOR-1</span>
    <span class="script-special script-special--hero">Special</span>
  </h1>

  <p class="gift-label">The perfect gift for You and Your Valentine.<br>Included In Your 30 Day Jumpstart:</p>

  <ul class="perks">
    <li><svg viewBox="0 0 20 18"><path d="M10,16 C4,11 1,8 1,5 C1,2 4,1 6,1 C8,1 9,2 10,4 C11,2 12,1 14,1 C16,1 19,2 19,5 C19,8 16,11 10,16 Z" fill="none" stroke="#fff" stroke-width="2"/></svg>Success Start Consultation</li>
    <li><svg viewBox="0 0 20 18"><path d="M10,16 C4,11 1,8 1,5 C1,2 4,1 6,1 C8,1 9,2 10,4 C11,2 12,1 14,1 C16,1 19,2 19,5 C19,8 16,11 10,16 Z" fill="none" stroke="#fff" stroke-width="2"/></svg>12 Group Personal Training<br>Sessions</li>
    <li><svg viewBox="0 0 20 18"><path d="M10,16 C4,11 1,8 1,5 C1,2 4,1 6,1 C8,1 9,2 10,4 C11,2 12,1 14,1 C16,1 19,2 19,5 C19,8 16,11 10,16 Z" fill="none" stroke="#fff" stroke-width="2"/></svg>Success Manual with Bonus<br>Nutrition Guide</li>
    <li><svg viewBox="0 0 20 18"><path d="M10,16 C4,11 1,8 1,5 C1,2 4,1 6,1 C8,1 9,2 10,4 C11,2 12,1 14,1 C16,1 19,2 19,5 C19,8 16,11 10,16 Z" fill="none" stroke="#fff" stroke-width="2"/></svg>Unlimited Coaching Support via<br>Private Members Group</li>
  </ul>

  <p class="tagline-couples">Couples that<br>Train Together<br>Stay Together.</p>

  <p class="brush-label">2-FOR-1<br>Valentine's Day</p>
  <span class="script-special script-special--badge">Special</span>
  <div class="price-badge">
    <div class="price-badge__only">Only</div>
    <div class="price-badge__amount">$99</div>
  </div>

  <p class="train-bar">This Valentine's Day Train Together!</p>

  <p class="slogan-pill">MOVE BETTER | LOOK BETTER | FEEL BETTER</p>
  <p class="expiry">Expires February 14th | Only 20 Spots Available</p>
  <p class="footer">Pulsora Bootcamps | 27 Elm Ave. Suite 8 Harmon CO 80000 | www.pulsorafit.com</p>
</main>
</body>
</html>
```